teaching love. a joyful state of being.

adding value to ones circumstance through the teachings of neutralization. quote for back of card: "and then it happens... One day you wake up and you're in this place. You are in this place where everything is right. Your heart is calm. Your soul is lit. Your thoughts are positive. Your vision is clear. Your faith is stronger than ever. And you are at peace. At peace with where you have been. At peace with what you've been through. And at peace with where you're headed." -unknown

Target Market(s)

spiritual, awakening, inspiration, motivation, gratefulness, oneness, peace, positive mindset,

Contact Information for Business Card

front: one line message from quote

Logo Text

up to suggestions

Font styles to use
Serif
Sans Serif
Script

Colors

Designer to choose colors to be used in the design.

Requirements
Must have
• entire quote on one side of card
Nice to have
• simple, and to the point
Should not have
• elaborated designs

```html
<!DOCTYPE html>
<html lang="en">
<head>
<meta charset="utf-8">
<title>Calm Harbor — Business Card</title>
<link rel="stylesheet" href="https://fonts.googleapis.com/css2?family=Arvo:wght@400;700&family=Noto+Serif:wght@400;700&display=swap">
<style>
  :root {
    --page-bg: #e6e6e8;
    --card-red: #fb0a1c;
    --card-red-soft: #fa7f86;
    --card-white: #ffffff;
    --logo-pink: #f5b3b3;
    --ink: #111111;
    --ink-dark-red: #3a0006;
    --rule-red: #d5101c;
  }
  * { box-sizing: border-box; margin: 0; padding: 0; }
  html, body { width: 1200px; height: 961px; overflow: hidden; }
  body { background: var(--page-bg); position: relative; }

  .card {
    position: absolute;
    width: 600px;
    height: 343px;
    border-radius: 28px;
    overflow: hidden;
    box-shadow: 0 6px 18px rgba(0,0,0,0.12);
  }

  /* Back of card: full quote */
  .card-back {
    left: 540px; top: 70px;
    background: var(--card-red);
    display: flex; flex-direction: column; align-items: center; justify-content: center;
    padding: 26px 40px;
    text-align: center;
    color: var(--card-white);
    font-family: "Arvo", Georgia, serif;
  }
  .quote-text { font-size: 16.5px; font-weight: 700; line-height: 1.32; letter-spacing: 0.2px; }
  .quote-source { font-size: 16.5px; font-weight: 700; margin-top: 2px; }

  /* Front of card */
  .card-front { left: 60px; top: 520px; background: var(--card-white); }
  .front-shapes { position: absolute; inset: 0; }

  .brand { position: absolute; left: 42px; top: 42px; display: flex; align-items: center; gap: 16px; }
  .brand-dot { width: 44px; height: 44px; border-radius: 50%; background: var(--logo-pink); }
  .brand-name {
    font-family: "Arvo", Georgia, serif; font-weight: 400;
    font-size: 36px; line-height: 1.08; color: var(--logo-pink);
  }

  .person { position: absolute; left: 372px; top: 92px; }
  .person-name { font-family: "Noto Serif", Georgia, serif; font-size: 30px; color: var(--card-white); }
  .person-role { font-family: "Noto Serif", Georgia, serif; font-size: 19px; font-weight: 700; color: var(--ink); margin-left: 72px; margin-top: -4px; }

  .address {
    position: absolute; left: 372px; top: 214px;
    display: flex; gap: 10px; align-items: flex-start;
    font-family: "Noto Serif", Georgia, serif; font-size: 14.5px; line-height: 1.25; color: var(--ink-dark-red);
  }
  .address svg { flex: none; margin-top: 2px; }

  .contacts { position: absolute; left: 30px; top: 222px; list-style: none; }
  .contacts li {
    display: flex; align-items: center; gap: 14px;
    font-family: "Noto Serif", Georgia, serif; font-size: 15.5px; color: var(--ink);
    height: 24px;
  }
  .contacts svg { flex: none; }
</style>
</head>
<body>

  <section class="card card-back" aria-label="Card back with quote">
    <p class="quote-text">" and then it happens... One day you wake up and you're in this place. You are in this place where everything is right. Your heart is calm. Your soul is lit. Your thoughts are positive. Your vision is clear. Your faith is stronger than ever. And you are at peace. At peace with where you have been. At peace with what you've been through. And at peace with where you're headed."</p>
    <p class="quote-source">-unknown</p>
  </section>

  <section class="card card-front" aria-label="Card front">
    <svg class="front-shapes" width="600" height="343" viewBox="0 0 600 343" aria-hidden="true">
      <path d="M292 0 C228 110 262 250 430 343 L600 343 L600 0 Z" fill="var(--card-red-soft)"/>
      <path d="M318 0 C258 110 290 250 462 343 L600 343 L600 0 Z" fill="var(--card-red)"/>
      <line x1="0" y1="198" x2="600" y2="198" stroke="var(--rule-red)" stroke-width="2"/>
      <line x1="355" y1="170" x2="575" y2="170" stroke="var(--card-white)" stroke-width="1.5"/>
    </svg>

    <div class="brand">
      <span class="brand-dot"></span>
      <span class="brand-name">Calm<br>Harbor</span>
    </div>

    <div class="person">
      <p class="person-name">Nyokabi Wairimu</p>
      <p class="person-role">Manager</p>
    </div>

    <div class="address">
      <svg width="14" height="18" viewBox="0 0 14 18" aria-hidden="true">
        <path d="M7 1 C3.5 1 1 3.6 1 6.8 C1 11 7 17 7 17 C7 17 13 11 13 6.8 C13 3.6 10.5 1 7 1 Z" fill="none" stroke="var(--ink-dark-red)" stroke-width="1.3"/>
        <circle cx="7" cy="6.8" r="2.2" fill="none" stroke="var(--ink-dark-red)" stroke-width="1.3"/>
      </svg>
      <span>Street Name, Suit 1234<br>State, Zip Code, Country</span>
    </div>

    <ul class="contacts">
      <li>
        <svg width="14" height="20" viewBox="0 0 14 20" aria-hidden="true">
          <rect x="1.5" y="1" width="11" height="18" rx="2" fill="none" stroke="var(--ink)" stroke-width="1.5"/>
          <line x1="5.5" y1="16" x2="8.5" y2="16" stroke="var(--ink)" stroke-width="1.5"/>
        </svg>
        <span>+254 700 555010</span>
      </li>
      <li>
        <svg width="16" height="16" viewBox="0 0 16 16" aria-hidden="true">
          <circle cx="8" cy="8" r="8" fill="var(--ink)"/>
          <rect x="3.5" y="5" width="9" height="6.5" fill="var(--card-white)"/>
          <path d="M3.5 5 L8 8.8 L12.5 5" fill="none" stroke="var(--ink)" stroke-width="1"/>
        </svg>
        <span>hello@calmharbor.org</span>
      </li>
      <li>
        <svg width="16" height="16" viewBox="0 0 16 16" aria-hidden="true">
          <circle cx="8" cy="8" r="7.2" fill="none" stroke="var(--ink)" stroke-width="1.4"/>
          <ellipse cx="8" cy="8" rx="3" ry="7.2" fill="none" stroke="var(--ink)" stroke-width="1"/>
          <line x1="0.8" y1="8" x2="15.2" y2="8" stroke="var(--ink)" stroke-width="1"/>
        </svg>
        <span>www.yourdomain.com</span>
      </li>
    </ul>
  </section>

</body>
</html>
```